Business card design for a world class martial arts and group fitness facility

We need a professional and eye catching design for a business card. The card will be used in networking as well as marketing.
We are a martial arts facility offering Taekwondo, Brazilian Jiu Jitsu, and group fitness. All of our programs are geared for kids and adults.
Our Taekwondo program is lead by a Hall of Fame instructor who was Instructor of the Year in 2015.
Our Brazilian Jiu Jitsu program is lead by a wold class instructor who is also a part of the renown Brazilian KVO team.
We offer 3 focused group fitness programs: Ring striking, Pulse Fitness, and The Meadow which are all lead by certified instructors in a small group setting.
Our facility is state of the art and has been recognized as such in nationally published magazines.
Our business is named The Lantern which is the linear logo that is attached. This is the main logo. I also attached a circular logo we have used in some marketing material. Our Jiu Jitsu program is the KVO team logo. The Taekwondo program is the TORVEX Prime. It would be nice to somehow incorporate all 3 logos, but The Lantern is most important.
Industry/Entity Type
Martial Art
Contact Information for Business Card
We would like to use all 3 logos if possible but The Lantern is the most important. We would like to have a place for a staff member's name while keeping the focus on the programs we offer.
Look and feel
Each slider illustrates characteristics of the customer's brand and the style your logo design should communicate.

```html
<!DOCTYPE html>
<html lang="en">
<head>
<meta charset="utf-8">
<title>The Lantern – Business Card</title>
<link rel="stylesheet" href="https://fonts.googleapis.com/css2?family=Open+Sans:wght@400;600;800&display=swap">
<style>
  :root {
    --canvas: #ecebe8;
    --card-white: #ffffff;
    --card-black: #000000;
    --brick: #7a2412;
    --ink: #111111;
    --paper-text: #ffffff;
    --badge-ring: #c8202a;
  }
  * { margin: 0; padding: 0; box-sizing: border-box; }
  html, body { width: 1200px; height: 900px; overflow: hidden; }
  body {
    background: var(--canvas);
    font-family: "Open Sans", Arial, sans-serif;
    position: relative;
  }
  .card {
    position: absolute;
    overflow: hidden;
    box-shadow: 0 6px 18px rgba(0,0,0,0.18);
  }

  /* Front card */
  .card-front {
    left: 78px; top: 35px; width: 588px; height: 362px;
    background: var(--card-white);
  }
  .card-front .bands { position: absolute; inset: 0; }
  .brand {
    position: absolute;
    display: flex; align-items: flex-end; gap: 14px;
    font-weight: 800; line-height: 1;
  }
  .brand-mark { display: flex; flex-direction: column; }
  .brand-the { font-size: 17px; letter-spacing: 0.5px; margin-left: 4px; margin-bottom: 2px; }
  .brand-name { font-size: 80px; letter-spacing: -1px; }
  .brand-square { width: 22px; height: 22px; background: var(--brick); margin-bottom: 10px; }
  .card-front .brand { left: 96px; top: 40px; color: var(--ink); }

  .staff {
    position: absolute; right: 310px; top: 260px; text-align: right; color: var(--paper-text);
  }
  .staff-name { font-size: 20px; font-weight: 600; line-height: 1.2; }
  .staff-role { font-size: 15px; font-weight: 400; line-height: 1.3; }

  .contact {
    position: absolute; left: 298px; top: 249px; list-style: none; color: var(--paper-text);
    font-size: 15.5px;
  }
  .contact li { display: flex; align-items: center; height: 21px; }
  .contact svg { width: 12px; height: 12px; margin-right: 12px; fill: var(--paper-text); }
  .address {
    position: absolute; left: 110px; top: 327px; color: var(--paper-text); font-size: 15.5px;
  }

  /* Back card */
  .card-back {
    left: 388px; top: 505px; width: 566px; height: 352px;
    background: var(--card-black);
  }
  .card-back .brand { left: 92px; top: 116px; color: var(--paper-text); }
  .programs {
    position: absolute; left: 0; right: 0; top: 262px;
    display: flex; justify-content: center; gap: 34px;
  }
  .program {
    display: flex; align-items: center; gap: 10px;
    color: var(--paper-text); font-size: 15px; font-weight: 600;
  }
  .program-ring {
    width: 56px; height: 56px; border-radius: 50%;
    border: 3px solid var(--badge-ring); background: var(--card-black);
  }
  .program-ring.light { border-color: var(--paper-text); }
</style>
</head>
<body>

<section class="card card-front" aria-label="Business card front">
  <svg class="bands" width="588" height="362" viewBox="0 0 588 362" aria-hidden="true">
    <polygon points="0,198 402,198 386,222 0,222" fill="var(--brick)"/>
    <polygon points="0,226 386,226 414,190 588,190 588,362 0,362" fill="var(--card-black)"/>
  </svg>

  <div class="brand">
    <div class="brand-mark">
      <span class="brand-the">THE</span>
      <span class="brand-name">LANTERN</span>
    </div>
    <span class="brand-square"></span>
  </div>

  <div class="staff">
    <p class="staff-name">Marcus Hale</p>
    <p class="staff-role">Managing Director</p>
  </div>

  <ul class="contact">
    <li>
      <svg viewBox="0 0 24 24"><path d="M6.6 10.8a15.1 15.1 0 0 0 6.6 6.6l2.2-2.2a1 1 0 0 1 1-.25 11.4 11.4 0 0 0 3.6.57 1 1 0 0 1 1 1V20a1 1 0 0 1-1 1A17 17 0 0 1 3 4a1 1 0 0 1 1-1h3.5a1 1 0 0 1 1 1c0 1.25.2 2.45.57 3.57a1 1 0 0 1-.25 1z"/></svg>
      044-555 018 274
    </li>
    <li>
      <svg viewBox="0 0 24 24"><path d="M2 5h20v14H2z M2 5l10 8 10-8" /><path d="M2 5l10 8 10-8v2l-10 8L2 7z" fill="#000"/></svg>
      info@lanterngym.com
    </li>
    <li>
      <svg viewBox="0 0 24 24"><path d="M12 2a10 10 0 1 0 0 20 10 10 0 0 0 0-20zm6.9 6h-2.9a15.6 15.6 0 0 0-1.4-3.6A8 8 0 0 1 18.9 8zM12 4c.8 1.2 1.5 2.5 1.9 4h-3.8c.4-1.5 1.1-2.8 1.9-4zM4.3 14a8 8 0 0 1 0-4h3.4a16 16 0 0 0 0 4zm.8 2h2.9c.3 1.3.8 2.5 1.4 3.6A8 8 0 0 1 5.1 16zM8 8H5.1a8 8 0 0 1 4.3-3.6C8.8 5.5 8.3 6.7 8 8zm4 12c-.8-1.2-1.5-2.5-1.9-4h3.8c-.4 1.5-1.1 2.8-1.9 4zm2.3-6H9.7a14.6 14.6 0 0 1 0-4h4.6a14.6 14.6 0 0 1 0 4zm.3 5.6c.6-1.1 1.1-2.3 1.4-3.6h2.9a8 8 0 0 1-4.3 3.6zm1.7-5.6a16 16 0 0 0 0-4h3.4a8 8 0 0 1 0 4z"/></svg>
      www.lanterngym.com
    </li>
  </ul>

  <p class="address">4820, Harbor Row Eastfield, Norland, 550192.</p>
</section>

<section class="card card-back" aria-label="Business card back">
  <div class="brand">
    <div class="brand-mark">
      <span class="brand-the">THE</span>
      <span class="brand-name">LANTERN</span>
    </div>
    <span class="brand-square"></span>
  </div>

  <div class="programs">
    <div class="program">
      <span class="program-ring"></span>
      <span class="program-name">KVO</span>
    </div>
    <div class="program">
      <span class="program-ring light"></span>
      <span class="program-name">TORVEX Prime</span>
    </div>
  </div>
</section>

</body>
</html>
```